Customs House descriptive business cards

We require a two-sided business card that has a simple yet elegant design. We want to be able to promote our services as a customs house. This card should include our logo, contact info and services offered with the logo being on one side and the contact info and services on the flip side

Target Market(s)

Importers / exporters to and from the Bahamas

Industry/Entity Type

Logistics

Contact Information for Business Card

The front side of the card could have the logo and the flip side should have the other relevant info

Font styles to use
Serif

Colors

Designer to choose colors to be used in the design.

Requirements
Must have
• (Harbourline Agents Ltd) Logo, address and contact info also services:
• import customs clearance, Delivery & HAndling services,Florida pickups, Export packing & Crating Services, export customs clearance, Consulting

```html
<!DOCTYPE html>
<html lang="en">
<head>
<meta charset="utf-8">
<title>Harbourline Agents Ltd — Business Card</title>
<link rel="stylesheet" href="https://fonts.googleapis.com/css2?family=Oswald:wght@400;500&family=Open+Sans:wght@400&display=swap">
<style>
  :root {
    --page: #eceff0;
    --card: #ffffff;
    --brand-blue: #2f8de8;
    --brand-grey: #b8bfc1;
    --photo-deep: #1a2a66;
    --photo-mid: #3a3f8a;
    --photo-warm: #d98a3a;
    --ink: #1c1c1c;
    --icon: #3a3a3a;
    --on-photo: #ffffff;
  }
  html, body {
    margin: 0;
    width: 1200px;
    height: 1000px;
    overflow: hidden;
    background: var(--page);
  }
  .canvas { position: relative; width: 1200px; height: 1000px; }
  .card {
    position: absolute;
    left: 306px;
    width: 604px;
    background: var(--card);
    overflow: hidden;
  }
  .card-front { top: 106px; height: 336px; }
  .card-back { top: 523px; height: 338px; }

  .photo-area { position: absolute; inset: 0; }

  .services {
    position: absolute;
    right: 25px;
    top: 19px;
    margin: 0;
    padding: 0;
    list-style: none;
    text-align: right;
    font-family: "Oswald", sans-serif;
    font-weight: 400;
    font-size: 14px;
    line-height: 21.6px;
    letter-spacing: 0.3px;
    color: var(--on-photo);
    text-transform: uppercase;
  }
  .service-icons {
    position: absolute;
    left: 296px;
    top: 282px;
    display: flex;
    gap: 14px;
  }
  .service-icons svg { width: 44px; height: 44px; }

  .brand-front {
    position: absolute;
    left: 20px;
    top: 90px;
    width: 222px;
    text-align: center;
  }
  .brand-mark {
    width: 46px; height: 46px; border-radius: 50%;
    background: var(--brand-blue);
    margin: 0 auto 18px;
  }
  .brand-name {
    font-family: "Oswald", sans-serif;
    font-weight: 500;
    color: var(--brand-blue);
    text-transform: uppercase;
    margin: 0;
  }
  .brand-front .brand-name { font-size: 26px; line-height: 32px; letter-spacing: 1px; }

  .contact-list {
    position: absolute;
    left: 46px;
    top: 64px;
    margin: 0; padding: 0;
    list-style: none;
    font-family: "Open Sans", sans-serif;
    font-size: 11.5px;
    line-height: 14px;
    color: var(--ink);
  }
  .contact-item { position: absolute; left: 0; display: flex; align-items: flex-start; white-space: nowrap; }
  .contact-item svg { width: 20px; height: 20px; margin-right: 15px; flex: none; margin-top: -3px; }
  .contact-item span { display: block; }

  .brand-back {
    position: absolute;
    left: 330px;
    top: 110px;
    width: 240px;
    text-align: center;
  }
  .brand-back .brand-name { font-size: 36px; line-height: 42px; letter-spacing: 1.5px; }
</style>
</head>
<body>
<main class="canvas">

  <section class="card card-front" aria-label="Card front">
    <svg class="photo-area" viewBox="0 0 604 336" width="604" height="336" role="img" aria-label="Aerial night photograph of a container ship at port">
      <defs>
        <linearGradient id="photoTone" x1="0" y1="0" x2="1" y2="1">
          <stop offset="0" stop-color="var(--photo-deep)"/>
          <stop offset="0.45" stop-color="var(--photo-warm)"/>
          <stop offset="0.7" stop-color="var(--photo-mid)"/>
          <stop offset="1" stop-color="var(--photo-deep)"/>
        </linearGradient>
      </defs>
      <polygon points="166,0 604,0 604,336 269,336 259,251 394,116 224,108" fill="url(#photoTone)"/>
    </svg>

    <div class="brand-front">
      <div class="brand-mark"></div>
      <p class="brand-name">Harbourline<br>Agents Ltd</p>
    </div>

    <ul class="services">
      <li>Brokerage &amp; Clearance</li>
      <li>Import &amp; Export</li>
      <li>Freight Forwarding</li>
      <li>Packing &amp; Crating</li>
      <li>Consulting</li>
      <li>Doorstep Delivery</li>
    </ul>

    <div class="service-icons" aria-hidden="true">
      <svg viewBox="0 0 44 44" fill="none" stroke="#fff" stroke-width="2" stroke-linejoin="round">
        <path d="M8 26h28l-4 8H12z"/><path d="M14 26v-8h16v8"/><path d="M20 18v-6h4v6"/><path d="M6 38c4 2 6-2 10 0s6-2 10 0 6-2 10 0"/>
      </svg>
      <svg viewBox="0 0 44 44" fill="none" stroke="#fff" stroke-width="2">
        <circle cx="19" cy="22" r="13"/><path d="M6 22h26M19 9c-6 7-6 19 0 26M19 9c6 7 6 19 0 26"/><rect x="26" y="18" width="13" height="13" fill="var(--photo-mid)"/>
      </svg>
      <svg viewBox="0 0 44 44" fill="none" stroke="#fff" stroke-width="2" stroke-linejoin="round">
        <rect x="4" y="14" width="22" height="16"/><path d="M26 19h8l6 6v5H26z"/><circle cx="12" cy="32" r="3"/><circle cx="33" cy="32" r="3"/>
      </svg>
      <svg viewBox="0 0 44 44" fill="none" stroke="#fff" stroke-width="2" stroke-linejoin="round">
        <path d="M15 10l7-4 7 4v8l-7 4-7-4z"/><path d="M6 18v12l10 8M38 18v12l-10 8"/>
      </svg>
      <svg viewBox="0 0 44 44" fill="none" stroke="#fff" stroke-width="2" stroke-linejoin="round">
        <rect x="8" y="8" width="22" height="30" rx="2"/><path d="M14 16h10M14 22h8M14 28h5"/><circle cx="31" cy="31" r="7" fill="var(--photo-deep)"/><path d="M28 31l2 2 4-4"/>
      </svg>
    </div>
  </section>

  <section class="card card-back" aria-label="Card back">
    <ul class="contact-list">
      <li class="contact-item" style="top:6px">
        <svg viewBox="0 0 20 20" fill="none" stroke="var(--icon)" stroke-width="1.2" stroke-linejoin="round"><path d="M4 2l3 0 1.5 4-2 1.5c1 2.2 2.8 4 5 5L13 10.5l4 1.5v3c0 1-1 2-2 2C8.5 17 3 11.5 3 5c0-1 1-3 1-3z"/></svg>
        <div><span>Phone: 242-555-0148</span><span>Fax: 242-555-0148</span></div>
      </li>
      <li class="contact-item" style="top:52px">
        <svg viewBox="0 0 20 20" fill="none" stroke="var(--icon)" stroke-width="1.2"><path d="M10 19s-6-6.5-6-11a6 6 0 0112 0c0 4.5-6 11-6 11z"/><circle cx="10" cy="8" r="2"/></svg>
        <div><span>#48 Palm Ridge Road</span><span>Nassau, Bahamas</span></div>
      </li>
      <li class="contact-item" style="top:101px">
        <svg viewBox="0 0 20 20" fill="none" stroke="var(--icon)" stroke-width="1.2"><rect x="1" y="4" width="18" height="12"/><path d="M1 4l9 7 9-7"/></svg>
        <span>imports@harbourlineagents.com</span>
      </li>
      <li class="contact-item" style="top:142px">
        <svg viewBox="0 0 20 20" fill="none" stroke="var(--icon)" stroke-width="1.2"><circle cx="10" cy="10" r="8.5"/><path d="M1.5 10h17M10 1.5c-4 4.5-4 12.5 0 17M10 1.5c4 4.5 4 12.5 0 17"/></svg>
        <span>www.harbourlineagents.com</span>
      </li>
      <li class="contact-item" style="top:180px">
        <svg viewBox="0 0 20 20" fill="none" stroke="var(--icon)" stroke-width="1.2"><circle cx="10" cy="10" r="8.5"/></svg>
        <span>harbourlineagents</span>
      </li>
      <li class="contact-item" style="top:213px">
        <svg viewBox="0 0 20 20" fill="none" stroke="var(--icon)" stroke-width="1.2"><circle cx="10" cy="10" r="8.5"/></svg>
        <span>harbourlineagents</span>
      </li>
    </ul>

    <div class="brand-back">
      <div class="brand-mark" style="width:64px;height:64px"></div>
      <p class="brand-name">Harbourline<br>Agents Ltd</p>
    </div>
  </section>

</main>
</body>
</html>
```